Tamworth Logistics

Create a modern, simple, Elegant business card design for my business.

Services: Vexa Trucks, Transport, Contract Logistics,

Business

Include all details same as old card plus new website address: www.tamworthlogistics-demo.com.au

• Similar colors to Logo.

```html
<!DOCTYPE html>
<html lang="en">
<head>
<meta charset="utf-8">
<title>Tamworth Logistics – Business Card</title>
<link rel="stylesheet" href="https://fonts.googleapis.com/css2?family=Lato:wght@400;700&display=swap">
<style>
  :root {
    --backdrop: #3a3a3a;
    --brand-deep: #124a78;
    --brand-blue: #0a6da6;
    --brand-navy: #1d4f8a;
    --ink-grey: #6e6e6e;
    --text-grey: #5c5c5c;
    --rule-blue: #7f9cc0;
    --paper: #ffffff;
  }
  * { margin: 0; padding: 0; box-sizing: border-box; }
  html, body {
    width: 1200px; height: 810px; overflow: hidden;
    background: var(--backdrop);
    font-family: "Lato", Arial, sans-serif;
  }
  .canvas { position: relative; width: 1200px; height: 810px; }

  .card {
    position: absolute;
    width: 580px; height: 331px;
    box-shadow: 0 6px 18px rgba(0,0,0,.35);
  }

  /* Front */
  .card-front {
    left: 110px; top: 60px;
    background: linear-gradient(160deg, var(--brand-deep) 0%, var(--brand-blue) 100%);
    color: var(--paper);
    display: flex; flex-direction: column; align-items: center; justify-content: center;
  }
  .card-front .brand-name {
    font-size: 40px; font-weight: 700; letter-spacing: .5px;
  }
  .card-front .services {
    margin-top: 56px; font-size: 14px; font-weight: 400;
  }

  /* Back */
  .card-back {
    left: 510px; top: 420px;
    background: var(--paper);
  }
  .card-back .brand-name {
    position: absolute; left: 40px; top: 142px;
    font-size: 30px; font-weight: 700; color: var(--ink-grey);
  }
  .card-back .divider {
    position: absolute; left: 318px; top: 70px;
    width: 1px; height: 190px;
    background: linear-gradient(to bottom, transparent, var(--rule-blue) 30%, var(--rule-blue) 70%, transparent);
  }
  .contact-block {
    position: absolute; left: 340px; top: 88px;
  }
  .person-name { font-size: 21px; font-weight: 700; color: var(--brand-navy); }
  .person-role { font-size: 14px; color: var(--text-grey); margin-top: 2px; }
  .contact-list { list-style: none; margin-top: 14px; }
  .contact-list li {
    display: flex; align-items: center; gap: 7px;
    font-size: 12.5px; color: var(--text-grey); line-height: 22px;
  }
  .contact-list svg { width: 11px; height: 11px; flex: none; fill: var(--brand-navy); }
</style>
</head>
<body>
<main class="canvas">
  <section class="card card-front">
    <div class="brand-name">Tamworth Logistics</div>
    <p class="services">Services: Vexa Trucks, Transport, Contract Logistics</p>
  </section>

  <section class="card card-back">
    <div class="brand-name">Tamworth Logistics</div>
    <div class="divider"></div>
    <div class="contact-block">
      <div class="person-name">Daniel Reyes</div>
      <div class="person-role">President</div>
      <ul class="contact-list">
        <li>
          <svg viewBox="0 0 24 24" aria-hidden="true"><path d="M6.6 10.8a15.1 15.1 0 0 0 6.6 6.6l2.2-2.2c.3-.3.7-.4 1-.2 1.1.4 2.3.6 3.6.6.6 0 1 .4 1 1V20c0 .6-.4 1-1 1A17 17 0 0 1 3 4c0-.6.4-1 1-1h3.5c.6 0 1 .4 1 1 0 1.3.2 2.5.6 3.6.1.3 0 .7-.2 1z"/></svg>
          0400123456
        </li>
        <li>
          <svg viewBox="0 0 24 24" aria-hidden="true"><path d="M2 5h20v14H2z M3 6l9 7 9-7" fill="none" stroke="#1d4f8a" stroke-width="2"/></svg>
          Dan@tamworthlogistics-demo.com.au
        </li>
        <li>
          <svg viewBox="0 0 24 24" aria-hidden="true"><circle cx="12" cy="12" r="10"/><path d="M2 12h20M12 2c3 3 3 17 0 20M12 2c-3 3-3 17 0 20" fill="none" stroke="#fff" stroke-width="1.5"/></svg>
          www.tamworthlogistics-demo.com.au
        </li>
      </ul>
    </div>
  </section>
</main>
</body>
</html>
```